New Business Card Design Project

I have a logo I would like to use on the business card. I want something that will stand out and that will be remembered.

Target Market(s)

People who collect gems, minerals and crystals.

Contact Information for Business Card

email - mkthestonefalcon@vendrollo.com
phone # 917-406-2581

Font styles to use
Serif
Sans Serif
Decorative

Colors

Designer to choose colors to be used in the design.

Requirements
Must have
• The logo...two to choose from.
Nice to have
• An eye catching and memorable way to draw in people who collect gems minerals and crystals.

```html
<!DOCTYPE html>
<html lang="en">
<head>
<meta charset="utf-8">
<title>Halvane Geology – Business Card</title>
<link rel="stylesheet" href="https://fonts.googleapis.com/css2?family=Libre+Baskerville:wght@700&family=Open+Sans:wght@400;600&display=swap">
<style>
  :root {
    --page: #e6e3de;
    --paper: #f7f7f7;
    --ink: #141414;
    --blue: #3d4fa6;
    --black-card: #161616;
    --black-card-light: #2b2b2b;
    --faint: #e9e9e9;
  }
  * { margin: 0; padding: 0; box-sizing: border-box; }
  html, body { width: 1200px; height: 942px; overflow: hidden; }
  body {
    background: var(--page);
    font-family: "Open Sans", sans-serif;
    position: relative;
  }
  .card {
    position: absolute;
    top: 321px;
    width: 525px;
    height: 300px;
    overflow: hidden;
    box-shadow: 0 6px 18px rgba(0,0,0,.18);
  }
  /* Front */
  .card--front { left: 50px; background: var(--paper); }
  .front-decoration {
    position: absolute; right: -40px; bottom: 20px;
    width: 260px; height: 260px; border-radius: 50%;
    background: radial-gradient(circle, var(--faint) 0%, rgba(233,233,233,0) 70%);
  }
  .brand {
    position: absolute; left: 24px; top: 128px; width: 216px;
    display: flex; align-items: center; justify-content: center; gap: 9px;
  }
  .brand__mark {
    width: 14px; height: 14px; flex: none;
    border-radius: 50%; background: var(--ink);
  }
  .brand__name {
    font-weight: 600; font-size: 17px; line-height: 1.2;
    letter-spacing: .3px; color: var(--ink); white-space: nowrap;
  }
  .divider {
    position: absolute; left: 256px; top: 40px;
    width: 1.5px; height: 200px; background: var(--blue);
  }
  .contact { position: absolute; left: 278px; top: 62px; }
  .contact__name {
    font-family: "Libre Baskerville", serif; font-size: 22px; font-weight: 700;
    letter-spacing: 1px; color: var(--ink);
  }
  .contact__title {
    margin-top: 4px; font-size: 13px; letter-spacing: 1px;
    text-transform: uppercase; color: var(--blue);
  }
  .contact__list { list-style: none; margin-top: 26px; }
  .contact__item {
    display: flex; align-items: center; gap: 8px;
    font-size: 12.5px; color: var(--ink); margin-bottom: 8px; white-space: nowrap;
  }
  .contact__item svg { width: 13px; height: 13px; flex: none; }
  .front-band {
    position: absolute; left: 0; bottom: 0; width: 100%; height: 34px;
    background: var(--ink);
  }
  .front-band__social {
    position: absolute; right: 0; top: 0; height: 100%; width: 58%;
    background: var(--blue);
    clip-path: polygon(18px 0, 100% 0, 100% 100%, 0 100%);
    display: flex; align-items: center; gap: 10px; padding-left: 40px;
    color: #fff; font-size: 14px; letter-spacing: .5px;
  }
  .front-band__social .square {
    width: 12px; height: 12px; background: #fff; opacity: .85;
  }
  /* Back */
  .card--back {
    left: 625px;
    background: linear-gradient(135deg, var(--black-card-light) 0%, var(--black-card) 55%, #0c0c0c 100%);
  }
  .back-decoration {
    position: absolute; left: 50%; top: 50%;
    width: 300px; height: 300px; margin: -150px 0 0 -150px; border-radius: 50%;
    background: radial-gradient(circle, rgba(255,255,255,.05) 0%, rgba(255,255,255,0) 70%);
  }
  .card--back .brand { left: 154px; top: 118px; }
  .card--back .brand__mark { background: #fff; }
  .card--back .brand__name { color: #fff; }
  .website {
    position: absolute; left: 0; bottom: 42px; width: 100%; text-align: center;
    color: #e8e8e8; font-size: 14px; letter-spacing: 2.5px;
  }
</style>
</head>
<body>

<section class="card card--front" aria-label="Business card front">
  <div class="front-decoration" role="img" aria-label="Faint large brand emblem in the background"></div>
  <div class="brand">
    <span class="brand__mark"></span>
    <span class="brand__name">Halvane Geology</span>
  </div>
  <div class="divider"></div>
  <div class="contact">
    <div class="contact__name">YOUR NAME</div>
    <div class="contact__title">Job Title</div>
    <ul class="contact__list">
      <li class="contact__item">
        <svg viewBox="0 0 16 16" aria-hidden="true"><rect width="16" height="16" rx="2" fill="#3d4fa6"/><path d="M5 3.5l2 2-1 1.3c.6 1.3 1.6 2.3 2.9 2.9l1.3-1 2 2-1.2 1.6C7.6 12 4 8.4 3.7 4.7z" fill="#fff"/></svg>
        917-406-2581
      </li>
      <li class="contact__item">
        <svg viewBox="0 0 16 16" aria-hidden="true"><rect width="16" height="16" rx="2" fill="#3d4fa6"/><rect x="3" y="5" width="10" height="7" fill="none" stroke="#fff" stroke-width="1.2"/><path d="M3 5l5 4 5-4" fill="none" stroke="#fff" stroke-width="1.2"/></svg>
        mkthestonefalcon@vendrollo.com
      </li>
    </ul>
  </div>
  <div class="front-band">
    <div class="front-band__social"><span class="square"></span>/halvanegeology</div>
  </div>
</section>

<section class="card card--back" aria-label="Business card back">
  <div class="back-decoration" role="img" aria-label="Faint large brand emblem in the background"></div>
  <div class="brand">
    <span class="brand__mark"></span>
    <span class="brand__name">Halvane Geology</span>
  </div>
  <div class="website">www.yourwebsite.com</div>
</section>

</body>
</html>
```